Website for company called VORENTbio

We need a website for our new company called VORENTbio which developed a platform/technology to identify antigen-specific T cells (immune cells) which can be used for cancer therapy, autoimmunity, etc.

The platform is called VORENT and is rapid, versatile, unbiased, and inexpensive.

We have a semi-final logo although we are not completely set on color and font of text (attached).

Target Market(s)

Our target audience at the moment would be potential investors and VCs. We eventually are interested in getting attention from scientists and cell/immunotherapy companies.

Industry/Entity Type

Healthcare/Technology

Coding

Coded - Design and coding required

Number of Pages Required

1 page

Colors
0094D4
00A9DD
6FCCEA
C7EBF8
E9F6FB
00AB8E
00BBA5
67D7C9
C6EFE9
E9F9F6
E54698
E96AAD
F1A4CE
F9D9EA
FCEFF6
A7469A
B969AE
D3A5CF
EDDBEB
F8F0F9
6B429C
8869AF
B7A5CE
E3DAEB
F3F0F8

Requirements
Must have
• Landing page about the company, About us page, Technology page (could be merged with company landing page), Contact us page

```html
<!DOCTYPE html>
<html lang="en">
<head>
<meta charset="utf-8">
<title>VORENTbio — Precision Immune Targeting</title>
<link href="https://fonts.googleapis.com/css2?family=Poppins:wght@300;400;500;600&display=swap" rel="stylesheet">
<style>
:root{
  --ink:#111322;
  --muted:#3b3d4a;
  --white:#ffffff;
  --hero-top:#dfe2f8;
  --hero-mid:#9db8ee;
  --hero-low:#7d90e2;
  --hero-end:#7a7fdc;
  --accent:#8aa3e6;
  --panel:#5866d3;
  --panel-light:#9cb3ea;
  --card:#f7f7f8;
  --line:#c8c9d2;
  --footer:#dde5f8;
  --social:#3a55b8;
}
*{box-sizing:border-box;margin:0;padding:0}
html,body{width:1200px;height:4732px;overflow:hidden}
body{position:relative;font-family:"Poppins",sans-serif;color:var(--ink);background:var(--white)}
.abs{position:absolute}
.brand{display:flex;align-items:center;gap:8px;font-weight:600;font-size:26px;color:var(--ink);letter-spacing:-.3px}
.brand-dot{width:14px;height:14px;border-radius:50%;background:var(--ink)}
.pill{display:inline-flex;align-items:center;justify-content:center;gap:14px;border-radius:30px;font-size:14px;font-weight:500}
.pill svg{width:14px;height:10px}
.pill-white{background:var(--white);color:var(--ink)}
.pill-outline{border:1.5px solid var(--ink);color:var(--ink)}

/* hero + about */
.top-band{left:0;top:0;width:1200px;height:1636px;background:linear-gradient(180deg,var(--hero-top) 0%,var(--hero-mid) 22%,var(--hero-low) 55%,var(--hero-end) 100%)}
.header{left:96px;top:20px;width:1012px;height:36px;display:flex;justify-content:space-between;align-items:center}
.header-right{display:flex;align-items:center;gap:26px;font-size:12px}
.hero-art{left:450px;top:58px;width:620px;height:620px;border-radius:50%;background:radial-gradient(circle at 45% 40%,#c8c6f4 0%,#8c8fe6 45%,rgba(120,130,230,.25) 75%,rgba(120,130,230,0) 100%)}
.hero-title{left:189px;top:244px;font-size:68px;font-weight:400;line-height:76px;color:var(--white)}
.hero-rule{left:189px;top:425px;width:575px;height:1px;background:rgba(255,255,255,.7)}
.hero-sub{left:189px;top:449px;font-size:14px;color:var(--white)}
.hero-btn{left:189px;top:487px;width:272px;height:55px}

.side-nav{left:62px;top:910px;font-size:12px;line-height:28px;color:rgba(255,255,255,.7)}
.side-nav li{list-style:none;padding-left:12px}
.side-nav .current{color:var(--white);border-left:2px solid var(--white)}
.about-title{left:267px;top:835px;font-size:56px;font-weight:400;color:var(--white)}
.about-text{left:267px;top:920px;width:680px;font-size:14px;line-height:22px;color:var(--white)}
.about-h{font-size:22px;font-weight:400;color:var(--white)}
.about-p{font-size:13.5px;line-height:22.5px;color:var(--white);margin-top:10px}
.mission{left:267px;top:1022px;width:330px}
.values{left:766px;top:1022px;width:200px}
.about-btn{left:267px;top:1177px;width:166px;height:51px}
.photo{background:linear-gradient(135deg,#d9d3cc,#a89a8f)}
.photo-a{left:1033px;top:731px;width:167px;height:249px;background:linear-gradient(135deg,#e8ebee,#c9b8a8)}
.photo-b{left:96px;top:1266px;width:323px;height:147px;background:linear-gradient(135deg,#a79a8e,#d9b27e)}
.photo-c{left:766px;top:1353px;width:158px;height:150px;background:linear-gradient(135deg,#f2f2f2,#d8c3b5)}
.photo-d{left:983px;top:1136px;width:217px;height:290px;background:linear-gradient(135deg,#7a8a5e,#c6645a)}

/* intro */
.intro-title{left:96px;top:1740px;font-size:58px;font-weight:400}
.intro-text{left:96px;top:1822px;width:680px;font-size:14px;line-height:22.5px;color:var(--muted)}
.intro-btn{left:937px;top:1784px;width:167px;height:54px}
.step{top:1968px;height:372px;color:var(--white)}
.step-label{position:absolute;left:52px;top:266px;font-size:22px;font-weight:500}
.step-sub{position:absolute;left:53px;top:306px;font-size:13.5px}
.step-1{left:42px;width:375px;background:linear-gradient(135deg,#1a2a5a,#6a3fa0 50%,#3a6ab0)}
.step-2{left:436px;width:374px;background:radial-gradient(circle at 55% 35%,#a06a5a,#3a2a2a 60%,#141414)}
.step-3{left:825px;width:375px;background:linear-gradient(135deg,#0a0c12 40%,#3a6aa8 75%,#c02a2a)}
.progress{left:189px;top:2408px;width:1011px;height:4px;background:#eceef4}
.progress span{display:block;width:307px;height:4px;background:linear-gradient(90deg,#a9c3f0,#7d8fdf)}

/* benefits */
.benefits-title{left:187px;top:2510px;font-size:58px;font-weight:400}
.benefit{top:2676px;height:305px;background:var(--card);text-align:center}
.benefit svg{position:absolute;left:50%;top:50px;transform:translateX(-50%)}
.benefit h3{position:absolute;top:161px;left:0;right:0;font-size:19px;font-weight:500}
.benefit p{position:absolute;top:203px;left:40px;right:40px;font-size:12.5px;line-height:18.5px;color:var(--muted)}
.b1{left:42px;width:270px}.b2{left:325px;width:269px}.b3{left:605px;width:270px}.b4{left:886px;width:268px}

/* use cases */
.uses{left:0;top:3100px;width:597px;height:622px;background:var(--panel);color:var(--white)}
.uses-title{position:absolute;left:92px;top:88px;font-size:54px;font-weight:400}
.use{position:absolute;left:94px;width:380px}
.use h4{font-size:19px;font-weight:400}
.use p{font-size:12px;line-height:18px;margin-top:4px}
.uses-art{left:597px;top:3100px;width:603px;height:622px;background:radial-gradient(circle at 50% 50%,#2a6fc0 0%,#4b8ad8 22%,#8fb2ea 40%,#b6d2f2 100%)}

/* contact */
.connect-title{left:243px;top:3830px;font-size:58px;font-weight:400}
.connect-sub{left:243px;top:3912px;font-size:14px;color:var(--muted)}
.field{font-size:14px;color:var(--muted);border-bottom:1px solid #7a7c88;padding:0 4px 10px}
.f-name{left:243px;top:4017px;width:340px}
.f-mail{left:619px;top:4017px;width:340px}
.f-msg{left:243px;top:4077px;width:716px;height:150px}
.submit{left:243px;top:4256px;width:165px;height:52px}

/* footer */
.footer{left:0;top:4455px;width:1200px;height:277px;background:linear-gradient(135deg,#e4e9f8,#cfdcf5 60%,#e0e7f7)}
.footer .brand{position:absolute;left:96px;top:112px;font-size:30px}
.foot-nav{position:absolute;left:437px;top:110px;display:flex;gap:40px;font-size:13px}
.social{position:absolute;top:102px;width:30px;height:30px;border-radius:50%;background:var(--social)}
.foot-rule{position:absolute;left:92px;top:206px;width:1016px;height:1px;background:#b7bdd4}
.copy{position:absolute;left:92px;top:242px;font-size:12px}
.legal{position:absolute;right:92px;top:242px;font-size:12px;display:flex;gap:14px}
</style>
</head>
<body>

<div class="abs top-band"></div>
<div class="abs hero-art" role="img" aria-label="Translucent 3D molecular sphere rendering in blue and violet"></div>

<header class="abs header">
  <div class="brand"><span class="brand-dot"></span>vorentbio</div>
  <div class="header-right">
    <span>Menu</span>
    <svg width="30" height="10" viewBox="0 0 30 10"><path d="M0 1h30M8 9h22" stroke="#111322" stroke-width="1.4"/></svg>
    <svg width="12" height="12" viewBox="0 0 12 12"><circle cx="5" cy="5" r="3.8" fill="none" stroke="#111322" stroke-width="1.4"/><path d="M8 8l3 3" stroke="#111322" stroke-width="1.4"/></svg>
  </div>
</header>

<h1 class="abs hero-title">Precision Immune<br>Targeting Starts Here</h1>
<div class="abs hero-rule"></div>
<p class="abs hero-sub">Discover VORENT — a rapid, versatile, and affordable platform to identify antigen-specific T cells.</p>
<a class="abs pill pill-white hero-btn">Learn How VORENT Works <svg viewBox="0 0 14 10"><path d="M0 5h12M8 1l4 4-4 4" fill="none" stroke="#111322" stroke-width="1.3"/></svg></a>

<ul class="abs side-nav">
  <li>Home</li><li class="current">About</li><li>Technology</li><li>Contact</li>
</ul>
<h2 class="abs about-title">About VORENTbio</h2>
<p class="abs about-text">Founded by scientists and driven by innovation, VORENTbio is advancing the future of immune diagnostics. Our mission is to accelerate the discovery of therapeutic T cells and support breakthroughs in personalized medicine.</p>
<div class="abs mission">
  <h3 class="about-h">Our Mission</h3>
  <p class="about-p">To make immune profiling faster, smarter, and accessible for everyone developing the next generation of therapies.</p>
</div>
<div class="abs values">
  <h3 class="about-h">Our Values</h3>
  <p class="about-p">Scientific Integrity<br>Real-World Impact<br>Speed &amp; Simplicity<br>Collaboration</p>
</div>
<a class="abs pill pill-white about-btn">Read More <svg viewBox="0 0 14 10"><path d="M0 5h12M8 1l4 4-4 4" fill="none" stroke="#111322" stroke-width="1.3"/></svg></a>
<div class="abs photo-a" role="img" aria-label="Smiling older woman in soft daylight"></div>
<div class="abs photo-b" role="img" aria-label="Two women sharing a tablet on a sofa"></div>
<div class="abs photo-c" role="img" aria-label="Handshake close-up"></div>
<div class="abs photo-d" role="img" aria-label="Happy older couple outdoors"></div>

<h2 class="abs intro-title">Introducing VORENT</h2>
<p class="abs intro-text">VORENT is a proprietary platform designed to identify antigen-specific T cells — the immune system's most targeted weapons. Our method is rapid, unbiased, and cost-effective, enabling new insights across cancer, autoimmune, and infectious diseases.</p>
<a class="abs pill pill-outline intro-btn">Read More <svg viewBox="0 0 14 10"><path d="M0 5h12M8 1l4 4-4 4" fill="none" stroke="#111322" stroke-width="1.3"/></svg></a>

<div class="abs step step-1" role="img" aria-label="Microscopic illustration of cells in blue and purple"><span class="step-label">Isolate</span><span class="step-sub">T cells from patient samples</span></div>
<div class="abs step step-2" role="img" aria-label="Illustration of a virus particle"><span class="step-label">Expose</span><span class="step-sub">To antigen libraries</span></div>
<div class="abs step step-3" role="img" aria-label="Translucent human body figure with immune cells"><span class="step-label">Detect</span><span class="step-sub">Responsive T cells</span></div>
<div class="abs progress"><span></span></div>

<h2 class="abs benefits-title">Key Benefits:</h2>
<div class="abs benefit b1">
  <svg width="84" height="84" viewBox="0 0 84 84" fill="none" stroke="#8aa3e6" stroke-width="2"><circle cx="42" cy="42" r="40"/><circle cx="42" cy="42" r="32"/><path d="M42 22v20l10 12"/></svg>
  <h3>Rapid Results</h3><p>Quick detection of antigen-specific T cells for faster decision-making.</p>
</div>
<div class="abs benefit b2">
  <svg width="84" height="84" viewBox="0 0 84 84" fill="none" stroke="#8aa3e6" stroke-width="2"><path d="M22 44c-8-4-6-18 4-18 2-8 14-10 18-4 6-6 18-2 18 6 10 2 10 16 0 18-2 8-12 10-18 6-6 6-18 4-22-8z"/><path d="M32 34c4 2 6 6 4 10M48 30c-2 6 2 10 8 10M40 48c4-2 10 0 12 4"/></svg>
  <h3>Unbiased Detection</h3><p>Technology ensures neutral and accurate identification of immune cells.</p>
</div>
<div class="abs benefit b3">
  <svg width="84" height="84" viewBox="0 0 84 84" fill="none" stroke="#8aa3e6" stroke-width="2"><path d="M40 10l10 6-14 24-10-6zM34 46a12 12 0 1 0 18-10M22 74h40M28 66h28v8"/><circle cx="38" cy="54" r="4"/></svg>
  <h3>Versatile Applications</h3><p>Applicable in oncology, immunology, infectious diseases, and beyond.</p>
</div>
<div class="abs benefit b4">
  <svg width="84" height="84" viewBox="0 0 84 84" fill="none" stroke="#8aa3e6" stroke-width="2"><circle cx="42" cy="42" r="22"/><path d="M42 8v8M42 68v8M8 42h8M68 42h8M18 18l6 6M60 60l6 6M18 66l6-6M60 24l6-6"/><path d="M42 32v18M36 44l6 6 6-6"/></svg>
  <h3>Cost-Effective</h3><p>Affordable for wide research and clinical implementation.</p>
</div>

<section class="abs uses">
  <h2 class="uses-title">Use Cases</h2>
  <div class="use" style="top:180px"><h4>Cancer Immunotherapy</h4><p>Identify T cells for designing effective and personalized cancer treatments.</p></div>
  <div class="use" style="top:271px"><h4>Autoimmune Profiling</h4><p>Map misdirected immune responses in autoimmune conditions.</p></div>
  <div class="use" style="top:362px"><h4>Infectious Monitoring</h4><p>Track immune activity against infectious agents like viruses and bacteria.</p></div>
  <div class="use" style="top:453px"><h4>Vaccine Development</h4><p>Evaluate vaccine-induced T-cell responses for efficacy and safety.</p></div>
</section>
<div class="abs uses-art" role="img" aria-label="Blue 3D cell sphere over a soft blue gradient"></div>

<h2 class="abs connect-title">Let's Connect</h2>
<p class="abs connect-sub">Whether you're an investor, collaborator, or fellow innovator — we'd love to hear from you.</p>
<div class="abs field f-name">Your Name</div>
<div class="abs field f-mail">Your Email</div>
<div class="abs field f-msg">Your Message</div>
<a class="abs pill pill-outline submit">Submit Now <svg viewBox="0 0 14 10"><path d="M0 5h12M8 1l4 4-4 4" fill="none" stroke="#111322" stroke-width="1.3"/></svg></a>

<footer class="abs footer">
  <div class="brand"><span class="brand-dot"></span>vorentbio</div>
  <nav class="foot-nav"><span>Home</span><span>About</span><span>Technology</span><span>Contact</span></nav>
  <span class="social" style="left:1001px"></span>
  <span class="social" style="left:1038px"></span>
  <span class="social" style="left:1075px"></span>
  <div class="foot-rule"></div>
  <p class="copy">© 2025 VORENTbio. All rights reserved.</p>
  <div class="legal"><span>Privacy Policy</span><span>|</span><span>Terms of Use</span></div>
</footer>

</body>
</html>
```